Professional "Save the Date" Design

We are looking for a professional designer to create a clean, modern, and eye-catching "Save the Date" invitation that will be sent to a select group of physicians participating in our REVALIA Study.
Key Requirements:
The VORELL logo should be clearly featured and lead the branding.
The OBEN GRAFT TX logo should also appear but be subordinate to the VORELL logo.
The design should be professional, modern, and easy to read — no busy or cluttered layouts.
The final product will be used in email communications (PDF or image format).
The project is time-sensitive: we would like to have the final version completed by end of day tomorrow.
Deliverables:
Final design in high-resolution PDF and image formats (PNG or JPG).
Editable file (Adobe Illustrator, InDesign, or similar) if possible.
Details:
Monday, June 23, 2025
4:30-5:15pm EST
Name of Call: REVALIA Investigator Call
Location: Virtual (PELLO Call)
Please include this blurb as well: "Join us for a REVALIA Study Investigator Call as we welcome all participating sites and provide key information to support a successful launch. We’ll cover points of contact, upcoming study-related events, and next steps as we begin site activation."
Physicians
Medical Device

```html
<!DOCTYPE html>
<html lang="en">
<head>
<meta charset="UTF-8">
<title>REVALIA Investigator Call – Save the Date</title>
<link href="https://fonts.googleapis.com/css2?family=Barlow:wght@400;500;600&display=swap" rel="stylesheet">
<style>
  :root {
    --paper: #ffffff;
    --ink: #0d0d0d;
    --brand-green: #6cb33f;
    --partner-navy: #0f1d45;
  }
  * { margin: 0; padding: 0; box-sizing: border-box; }
  html, body {
    width: 900px;
    height: 1200px;
    overflow: hidden;
    background: var(--paper);
  }
  .invite {
    position: relative;
    width: 900px;
    height: 1200px;
    background: var(--paper);
    color: var(--ink);
    font-family: "Barlow", Arial, sans-serif;
  }
  .brand {
    position: absolute;
    font-weight: 500;
    line-height: 1;
    white-space: nowrap;
  }
  .brand--lead {
    left: 89px;
    top: 86px;
    font-size: 78px;
    color: var(--brand-green);
    letter-spacing: -1px;
  }
  .brand--partner {
    right: 94px;
    top: 112px;
    font-size: 38px;
    color: var(--partner-navy);
  }
  .headline {
    position: absolute;
    left: 0;
    width: 100%;
    text-align: center;
    line-height: 1;
    font-weight: 500;
  }
  .headline--save {
    top: 222px;
    font-size: 96px;
    letter-spacing: 1.5px;
  }
  .headline--study {
    top: 312px;
    font-size: 122px;
    letter-spacing: 2px;
  }
  .when {
    position: absolute;
    top: 458px;
    left: 0;
    width: 100%;
    text-align: center;
    font-size: 56px;
    font-weight: 500;
    line-height: 60px;
  }
  .blurb {
    position: absolute;
    top: 634px;
    left: 89px;
    width: 735px;
    font-size: 30px;
    font-weight: 400;
    letter-spacing: 0.6px;
    line-height: 36px;
    text-align: justify;
    text-align-last: center;
  }
  .schedule {
    position: absolute;
    top: 918px;
    left: 77px;
    font-size: 54px;
    font-weight: 500;
    line-height: 60px;
  }
  .venue {
    position: absolute;
    left: 584px;
    top: 934px;
    width: 200px;
    text-align: center;
  }
  .venue__dot {
    display: block;
    margin: 0 auto;
  }
  .venue__name {
    display: block;
    margin-top: 0;
    font-size: 56px;
    font-weight: 600;
    line-height: 1;
    color: var(--brand-green);
  }
</style>
</head>
<body>
  <main class="invite">
    <div class="brand brand--lead">VORELL</div>
    <div class="brand brand--partner">OBEN GRAFT TX</div>

    <h1 class="headline headline--save">Save the Date</h1>
    <h2 class="headline headline--study">REVALIA</h2>

    <p class="when">Monday, June 23, 2025<br>4:30-5:15pm EST</p>

    <p class="blurb">Join us for a REVALIA Study Investigator Call as we welcome all participating sites and provide key information to support a successful launch. We’ll cover points of contact, upcoming study-related events, and next steps as we begin site activation.</p>

    <p class="schedule">Monday,<br>16:30pm<br>17:15pm EST</p>

    <div class="venue">
      <svg class="venue__dot" width="114" height="114" viewBox="0 0 114 114" aria-hidden="true">
        <circle cx="57" cy="57" r="57" fill="var(--brand-green)"/>
      </svg>
      <span class="venue__name">PELLO</span>
    </div>
  </main>
</body>
</html>
```